Need Flyer for Our Real estate Agency

Need to run General Campaign for our agency with Start of New Year as our theme ..Must have an agent's picture on the DL..
Address:
9 / 386Barwin rd, Truganina VIC 3029
Ph:03 9142 7305
email:info@koridanrealestate.example.au
www.koridanrealestate.example.au
Something like as attached picture..
Target Market(s)
Home Buyers
Industry/Entity Type
Real Estate Agent
Requirements
Must have
- Our Logo Colours

```html
<!DOCTYPE html>
<html lang="en">
<head>
<meta charset="utf-8">
<title>Koridan Real Estate – DL Flyer</title>
<link rel="stylesheet" href="https://fonts.googleapis.com/css2?family=Montserrat:wght@400;900&family=Roboto:wght@400&display=swap">
<style>
  :root {
    --bg: #e4e4e4;
    --navy: #1f2252;
    --white: #ffffff;
    --photo-light: #e9eef0;
    --photo-mid: #c9d2d6;
    --photo-dark: #2a2c33;
  }
  * { box-sizing: border-box; margin: 0; padding: 0; }
  html, body { width: 1200px; height: 1000px; overflow: hidden; background: var(--bg); }
  .flyer {
    position: absolute; left: 50px; top: 240px;
    width: 1100px; height: 520px;
    display: flex; background: var(--navy);
    box-shadow: 0 6px 18px rgba(0,0,0,0.18);
  }
  .agent-photo {
    width: 460px; height: 100%;
    background: linear-gradient(160deg, var(--photo-light) 0%, var(--photo-mid) 45%, var(--photo-dark) 100%);
  }
  .info-panel { position: relative; flex: 1; color: var(--white); font-family: "Roboto", sans-serif; }
  .brand {
    position: absolute; top: 48px; right: 48px;
    display: flex; flex-direction: column; align-items: center; gap: 4px;
  }
  .brand-mark { width: 22px; height: 22px; border: 2px solid var(--white); }
  .brand-name { font-family: "Montserrat", sans-serif; font-weight: 400; font-size: 20px; letter-spacing: 5px; }
  .brand-tagline { font-size: 7px; letter-spacing: 1.5px; opacity: 0.8; }
  .headline {
    position: absolute; top: 170px; left: 40px; right: 40px;
    font-family: "Montserrat", sans-serif; font-weight: 900;
    font-size: 31px; line-height: 1.18; text-transform: uppercase; text-align: center;
  }
  .contacts {
    position: absolute; left: 40px; right: 48px; bottom: 44px;
    display: flex; justify-content: space-between; align-items: flex-end;
    font-size: 16px;
  }
  .contact-col { display: flex; flex-direction: column; gap: 6px; }
  .contact-col.right { margin-top: 22px; }
  .contact-line { display: flex; align-items: center; gap: 8px; }
  .contact-line svg { width: 16px; height: 16px; fill: var(--white); flex-shrink: 0; }
</style>
</head>
<body>
  <article class="flyer">
    <div class="agent-photo" role="img" aria-label="Portrait photograph of a smiling real estate agent in a dark suit seated at a desk in a bright office"></div>
    <section class="info-panel">
      <div class="brand">
        <span class="brand-mark"></span>
        <span class="brand-name">KORIDAN</span>
        <span class="brand-tagline">REAL ESTATE GROUP</span>
      </div>
      <h1 class="headline">Landlords grow rich in their sleep without working, risking or economising</h1>
      <div class="contacts">
        <div class="contact-col">
          <div class="contact-line">
            <svg viewBox="0 0 16 16"><path d="M8 1 0 8h2v7h4v-4h4v4h4V8h2z"/></svg>
            <span>9 / 386Barwin rd, Truganina VIC 3029</span>
          </div>
          <div class="contact-line">
            <svg viewBox="0 0 16 16"><path d="M3 1l3 3-2 2c1 2 4 5 6 6l2-2 3 3-2 2C7 15 1 9 1 3z"/></svg>
            <span>03 9142 7305</span>
          </div>
        </div>
        <div class="contact-col right">
          <div class="contact-line">
            <svg viewBox="0 0 16 16"><path d="M1 3h14v10H1zm1 1v1l6 4 6-4V4z"/></svg>
            <span>info@koridanrealestate.example.au</span>
          </div>
          <div class="contact-line">
            <svg viewBox="0 0 16 16"><path d="M8 1a7 7 0 100 14A7 7 0 008 1zm0 1.5c.9 1 1.5 2.5 1.7 4.5H6.3C6.5 5 7.1 3.5 8 2.5zM2.6 7h2.2c.1-1.7.5-3.1 1.1-4.1A5.5 5.5 0 002.6 7zm8.6 0h2.2a5.5 5.5 0 00-3.3-4.1c.6 1 1 2.4 1.1 4.1zM2.6 9a5.5 5.5 0 003.3 4.1c-.6-1-1-2.4-1.1-4.1zm3.7 0c.2 2 .8 3.5 1.7 4.5.9-1 1.5-2.5 1.7-4.5zm4.9 0c-.1 1.7-.5 3.1-1.1 4.1A5.5 5.5 0 0013.4 9z"/></svg>
            <span>www.koridanrealestate.example.au</span>
          </div>
        </div>
      </div>
    </section>
  </article>
</body>
</html>
```